Bright Hall Meetings: Educators and Families joining forces for pupil growth.

This is a book that helps to prepare for and hold a standard conference that an educator would have with the parents of the students in the school. It is also about how to have problem-solving conferences around difficult issues using techniques from family therapy. Parent involvement is a key ingredient for student success, but most educators have no training in holding meetings with parents. This book fills that gap.
Updates

Need extra days to review

Target Market(s)

Teachers, principals, counselors, school psychologists, school nurses. Anyone who has conferences with the parents of their students.

Font styles to use
Sans Serif

Colors
85acd3
ffcf3e

Requirements
Must have
• I have several books coming up. I'd like something that could be carried over to the new ones without too many changes. They won't all be about education. I am a psychologist so most of my writings will cover subjects related to emotional intelligence.
Nice to have
• Something dignified that will pop out for those in the schools. I like the combination of a royal blue background with white and gold (not yellow) lettering.
Should not have
• I'd like it to be easy to read. Not too messy or too much stuff on the page.

```html
<!DOCTYPE html>
<html lang="en">
<head>
<meta charset="utf-8">
<title>Bright Hall Meetings – Book Cover</title>
<link rel="stylesheet" href="https://fonts.googleapis.com/css2?family=Anton&family=Oswald:wght@600&family=Quicksand:wght@500;600&display=swap">
<style>
  :root {
    --stage: #1e1e1e;
    --cover-light: #bfe0ef;
    --cover-mid: #a9d3e8;
    --navy: #232c6b;
    --ink: #111111;
    --white: #ffffff;
  }
  html, body {
    margin: 0;
    padding: 0;
    overflow: hidden;
  }
  body {
    width: 1200px;
    height: 1200px;
    background: var(--stage);
    display: flex;
    align-items: center;
    justify-content: center;
  }
  .cover {
    position: relative;
    width: 760px;
    height: 1140px;
    background: linear-gradient(160deg, var(--cover-light) 0%, var(--cover-mid) 60%, #a4cfe4 100%);
    overflow: hidden;
  }
  .author-name {
    position: absolute;
    top: 205px;
    left: 0;
    right: 0;
    text-align: center;
    font-family: "Quicksand", sans-serif;
    font-weight: 600;
    font-size: 26px;
    letter-spacing: 0.55em;
    color: var(--ink);
    margin: 0;
    padding-left: 0.55em;
  }
  .title {
    position: absolute;
    top: 262px;
    left: 0;
    right: 0;
    margin: 0;
    text-align: center;
    color: var(--navy);
  }
  .title-line-one {
    display: block;
    font-family: "Oswald", sans-serif;
    font-weight: 600;
    font-size: 108px;
    line-height: 1.1;
    letter-spacing: -0.01em;
  }
  .title-line-two {
    display: block;
    font-family: "Anton", sans-serif;
    font-size: 128px;
    line-height: 1.05;
    letter-spacing: 0.005em;
    -webkit-text-stroke: 4px var(--white);
    paint-order: stroke fill;
  }
  .title-rule {
    position: absolute;
    top: 548px;
    left: 175px;
    width: 410px;
    height: 3px;
    background: var(--ink);
  }
  .subtitle {
    position: absolute;
    top: 572px;
    left: 60px;
    right: 60px;
    margin: 0;
    text-align: center;
    font-family: "Quicksand", sans-serif;
    font-weight: 600;
    font-size: 35px;
    line-height: 1.2;
    color: var(--ink);
  }
  .cover-photo {
    position: absolute;
    left: 0;
    right: 0;
    bottom: 0;
    height: 440px;
    background:
      linear-gradient(180deg, rgba(169,211,232,0) 0%, rgba(169,211,232,0) 30%, rgba(240,248,252,0.55) 45%, rgba(169,211,232,0) 60%),
      linear-gradient(180deg, var(--cover-mid) 0%, #dbeef7 35%, #3b4f95 55%, #1f2a6e 70%, #6e9cc9 85%, #cfe6f2 100%);
  }
</style>
</head>
<body>
  <main class="cover">
    <p class="author-name">AUTHOR NAME</p>
    <h1 class="title">
      <span class="title-line-one">Bright Hall</span>
      <span class="title-line-two">MEETINGS</span>
    </h1>
    <div class="title-rule"></div>
    <p class="subtitle">Educators and Families joining forces for pupil growth</p>
    <div class="cover-photo" role="img" aria-label="Blue-toned photo of a cheering presenter with arms raised behind a row of silhouetted audience members, blended with a city skyline"></div>
  </main>
</body>
</html>
```